Bordkarte MY Frelk
Unsere Ideen wurden sehr gut aufgenommen und in der Diskussion weiterentwickelt. Wir freuen uns, das Design einsetzen zu können
Zielgruppe
Bordkarte für ein Rentnerpaar, welches nahezu ganzjährig auf dem eigenen Motorschiff Nord- und Ostsee bereist.
Bei einer Bordkarte stehen Angaben zum Motorschiff im Fokus (Funkkennzeichen Identifikationsnummer)und nicht die des Eignerpaars das maximal mit Vornamen erscheint.
Die Karte wird anderen Eignern abgegeben und dient dazu, dass man sich auch auf grosse Distanzen suchen und kontaktieren kann. So wird bei diesen meist Einzelgängern das soziale Umfeld gepflegt.
Für nicht Berner, 'Frelk' ist Dialekt und bedeutet 'Bär'
Aufgabenstellung
Originelles*, maritimes Sujet oder markantes, nördliches Sternzeichen
(*keine Anker oder Muscheln!)
Maritimes Design, zurückhaltend, repräsentativ.
Die Karte soll das Gefühl der Ruhe und Zufriedenheit vermitteln
Schiff und Namesdesign als Bilder im Anhang. Die Rechte für das Wappen, habe ich einmalig für den Namen erworben.
MY Frelk
Henrike & Olaf
MMSI: 471.803.915
CS: KQRT7
InmarSat : 004926 81037

```html
<!DOCTYPE html>
<html lang="de">
<head>
<meta charset="utf-8">
<title>Bordpass MY Frelk</title>
<link rel="stylesheet" href="https://fonts.googleapis.com/css2?family=Montserrat:wght@300;700;800&display=swap">
<style>
  :root {
    --paper: #ebebeb;
    --title-grey: #bdbdbd;
    --ink: #0a0a0a;
    --owners-grey: #b5b5b5;
    --hull-grey: #9ea4a8;
    --hull-light: #c9cccd;
    --cabin-blue: #4f5f70;
    --window-blue: #3b4a5c;
    --deck-sand: #e2dcc0;
    --crest-red: #8e2a1c;
    --crest-edge: #a3a3a3;
  }
  * { margin: 0; padding: 0; box-sizing: border-box; }
  html, body {
    width: 800px; height: 1200px; overflow: hidden;
    background: var(--paper);
  }
  .card {
    position: relative; width: 800px; height: 1200px;
    background: var(--paper); overflow: hidden;
    font-family: "Montserrat", sans-serif;
  }
  .vessel-photo {
    position: absolute; left: 0; top: 104px; width: 800px; height: 456px;
    background:
      linear-gradient(180deg, rgba(235,235,235,0) 0%, rgba(235,235,235,0) 45%, rgba(235,235,235,0.7) 75%, var(--paper) 100%),
      radial-gradient(ellipse 260px 110px at 620px 170px, rgba(59,74,92,0.85), rgba(59,74,92,0) 100%),
      radial-gradient(ellipse 180px 90px at 380px 200px, rgba(59,74,92,0.75), rgba(59,74,92,0) 100%),
      radial-gradient(ellipse 140px 110px at 70px 200px, rgba(79,95,112,0.7), rgba(79,95,112,0) 100%),
      radial-gradient(ellipse 300px 160px at 700px 320px, rgba(226,220,192,0.9), rgba(226,220,192,0) 100%),
      linear-gradient(180deg, var(--hull-light) 0%, var(--hull-grey) 40%, #8f969c 70%, var(--hull-light) 100%);
  }
  .card-title {
    position: absolute; left: 0; top: 0; width: 800px; height: 110px;
  }
  .card-title text {
    font-family: "Montserrat", sans-serif; font-weight: 700;
    fill: var(--title-grey);
  }
  .vessel-data {
    position: absolute; left: 0; top: 640px; width: 800px; height: 320px;
  }
  .vessel-data text { font-family: "Montserrat", sans-serif; font-size: 70px; fill: var(--ink); }
  .vessel-data .label { font-weight: 800; letter-spacing: -2px; }
  .vessel-data .value { font-weight: 300; }
  .rule {
    position: absolute; left: 0; top: 1042px; width: 800px; height: 2px;
    background: var(--ink);
  }
  .owners {
    position: absolute; left: 0; top: 1070px; width: 680px; height: 100px;
  }
  .owners text { font-family: "Montserrat", sans-serif; font-size: 70px; fill: var(--owners-grey); }
  .owners .name { font-weight: 800; }
  .owners .amp { font-weight: 300; }
  .crest-mark {
    position: absolute; left: 686px; top: 1066px; width: 100px; height: 112px;
    background: var(--crest-red); border: 5px solid var(--crest-edge);
  }
</style>
</head>
<body>
  <main class="card">
    <svg class="card-title" viewBox="0 0 800 110" aria-label="Bordpass">
      <text x="0" y="98" font-size="172" textLength="800" lengthAdjust="spacingAndGlyphs">BORDPASS</text>
    </svg>

    <div class="vessel-photo" role="img" aria-label="Foto des Motorschiffs Frelk: Steuerhaus mit grossen Fenstern, Reling und Bootsname am Aufbau, nach unten ausgeblendet"></div>

    <svg class="vessel-data" viewBox="0 640 800 320" aria-label="Schiffsdaten">
      <text y="725"><tspan class="label" x="0">MY</tspan><tspan class="value" x="108" textLength="160" lengthAdjust="spacingAndGlyphs">Frelk</tspan></text>
      <text y="797"><tspan class="label" x="0">MMSI</tspan><tspan class="value" x="190" textLength="442" lengthAdjust="spacingAndGlyphs">471.803.915</tspan></text>
      <text y="867"><tspan class="label" x="0">CS</tspan><tspan class="value" x="96" textLength="244" lengthAdjust="spacingAndGlyphs">KQRT7</tspan></text>
      <text y="940"><tspan class="label" x="0">InmarSat</tspan><tspan class="value" x="320" textLength="480" lengthAdjust="spacingAndGlyphs">00492681037</tspan></text>
    </svg>

    <div class="rule"></div>

    <svg class="owners" viewBox="0 1070 680 100" aria-label="Henrike und Olaf">
      <text y="1148"><tspan class="name" x="8">HENRIKE</tspan><tspan class="amp">&amp;</tspan><tspan class="name">OLAF</tspan></text>
    </svg>
    <div class="crest-mark" role="img" aria-label="Wappen der Eigner"></div>
  </main>
</body>
</html>
```